Business Card Design for Varnok Facility Services

We are looking for a Business Card Design for the Company "Varnok Facility Services."
Front side:
- Company Logo (small)
- Company Name, address, pohone, website and personal data.
- white background, for text e.g. company colors (blue or green like in the logo)
Please use following data:
Company data:
Varnok Facility Services Tulbrecht
Kirchmattweg 12
6331 Cham
www.varnok-fs.ch
Person data:
Ruben Tulbrecht
Geschäftsführer
+41 76 519 84 60
info@varnok-fs.ch
Back side:
could be colored in blue or green
please use a big logo sing and some smaller icons to say what is all beeing offered in facility services, like cleaning, maintenance cleaning
industrial cleaning, caretaking, gardening, disposal. There is no need for everyone of the icons if there are similar or an icon is standing for more of them.
Cleaning Service
colors to use:
blue: HEX 246BB0
green: HEX 52B33E

```html
<!DOCTYPE html>
<html lang="de">
<head>
<meta charset="utf-8">
<title>Varnok Facility Services – Business Card</title>
<link rel="stylesheet" href="https://fonts.googleapis.com/css2?family=Open+Sans:wght@400;600;700&display=swap">
<style>
  :root {
    --brand-blue: #246BB0;
    --brand-green: #52B33E;
    --card-white: #f1f1ef;
    --backdrop: #3a3b3d;
  }
  * { margin: 0; padding: 0; box-sizing: border-box; }
  html, body { width: 1200px; height: 901px; overflow: hidden; }
  body {
    background: var(--backdrop);
    font-family: "Open Sans", Arial, sans-serif;
    display: flex;
    align-items: center;
    justify-content: center;
    gap: 40px;
  }
  .card {
    position: relative;
    width: 540px;
    height: 309px;
    overflow: hidden;
    box-shadow: 0 10px 24px rgba(0,0,0,.35);
  }
  .card-front { background: var(--brand-green); }
  .front-shape { position: absolute; inset: 0; }
  .contact-block {
    position: absolute;
    left: 262px;
    top: 58px;
    color: var(--brand-blue);
  }
  .person-name {
    font-weight: 700;
    font-size: 19px;
    letter-spacing: .5px;
    text-transform: uppercase;
    line-height: 1.1;
  }
  .person-title {
    color: var(--brand-green);
    font-size: 16px;
    margin-bottom: 10px;
  }
  .contact-list { list-style: none; font-size: 14px; line-height: 20px; }
  .contact-list li { display: flex; align-items: flex-start; gap: 8px; }
  .contact-icon {
    flex: none; width: 14px; height: 14px; margin-top: 3px;
  }
  .is-green { color: var(--brand-green); }
  .is-blue { color: var(--brand-blue); }

  .card-back {
    background: var(--brand-green);
    color: #fff;
    display: flex;
    flex-direction: column;
    align-items: center;
    justify-content: center;
    text-align: center;
  }
  .brand-name {
    font-weight: 600;
    font-size: 30px;
    letter-spacing: 1px;
    margin-bottom: 26px;
  }
  .service-list {
    font-size: 16px;
    line-height: 24px;
    color: rgba(255,255,255,.92);
  }
</style>
</head>
<body>

  <section class="card card-front" aria-label="Business card front">
    <svg class="front-shape" viewBox="0 0 540 309" aria-hidden="true">
      <circle cx="640" cy="250" r="470" fill="var(--brand-blue)"/>
      <circle cx="640" cy="250" r="461" fill="var(--card-white)"/>
      <circle cx="640" cy="250" r="454" fill="var(--card-white)"/>
    </svg>
    <div class="contact-block">
      <p class="person-name">Ruben Tulbrecht</p>
      <p class="person-title">Geschäftsführer</p>
      <ul class="contact-list">
        <li>
          <svg class="contact-icon is-green" viewBox="0 0 14 14" aria-hidden="true"><rect width="14" height="14" rx="2" fill="currentColor"/><circle cx="7" cy="5.5" r="2.5" fill="#fff"/><path d="M3 12c.5-2.5 2-3.5 4-3.5s3.5 1 4 3.5z" fill="#fff"/></svg>
          <span>Varnok Facility Services Tulbrecht<br>Kirchmattweg 12, 6331 Cham</span>
        </li>
        <li class="is-green">
          <svg class="contact-icon is-blue" viewBox="0 0 14 14" aria-hidden="true"><rect width="14" height="14" rx="2" fill="currentColor"/><path d="M4.5 3l1.8 2-1 1.2c.6 1.2 1.4 2 2.6 2.6l1.2-1 2 1.8-1 1.6c-3.4-.3-6.2-3.1-6.5-6.5z" fill="#fff"/></svg>
          <span>+41 76 519 84 60</span>
        </li>
        <li class="is-green">
          <svg class="contact-icon is-blue" viewBox="0 0 14 14" aria-hidden="true"><rect width="14" height="14" rx="2" fill="currentColor"/><rect x="2.5" y="4" width="9" height="6" fill="none" stroke="#fff"/><path d="M2.5 4l4.5 3.5L11.5 4" fill="none" stroke="#fff"/></svg>
          <span>info@varnok-fs.ch</span>
        </li>
        <li>
          <svg class="contact-icon is-green" viewBox="0 0 14 14" aria-hidden="true"><rect width="14" height="14" rx="2" fill="currentColor"/><path d="M7 2.5l4.5 4h-1.3V11H8.3V8.3H5.7V11H3.8V6.5H2.5z" fill="#fff"/></svg>
          <span>www.varnok-fs.ch</span>
        </li>
      </ul>
    </div>
  </section>

  <section class="card card-back" aria-label="Business card back">
    <p class="brand-name">Varnok Facility Services</p>
    <p class="service-list">Cleaning . Maintenance Cleaning<br>Industrial Cleaning . Caretaking . Gardening . Disposal</p>
  </section>

</body>
</html>
```